Commit To Be The Best! - Marketing, Training, Managment for Multifamily Professionals

Flyer for training event. I have to be able to edit location, times, speakers, cost,
We will have 2 to 4 speakers for each event. Each event may have a different topic relating to the main topic (Marketing, Training, Management). The idea is to get as many people to open or pick up the fly and say "I have to attend" this seminar. We are the experts in the industry and want to portray this with the flyer. Each speaker will have a topic and a certain amount of time. Each topic will be different.
Updates

Project Deadline Extended
Reason: I apologize for the new design deadline. I've been traveling extensively for work and unable to view submissions. Currently I am not traveling and able to dedicate time to view all of the wonderful submissions. I'm looking forward to selecting one. Thank you all for your understanding.

Target Market(s)

Multifamily - Apartment Communities, Owners, Apartment Associations, Leasing Agents, Marketing Directors, Managers, Presidents,

Industry/Entity Type

Marketing

Colors

Designer to choose colors to be used in the design.

Requirements
Must have
• Editable flyer. I have to be able to edit; location, times/date, speaker, cost, description.
• Sponsored by Volt Harbor Power attached Logo for VHP
Nice to have
• Spot for photo of each speaker (2-4) speaker

```html
<!DOCTYPE html>
<html lang="en">
<head>
<meta charset="utf-8">
<title>Training Event Flyer</title>
<link rel="stylesheet" href="https://fonts.googleapis.com/css2?family=Bebas+Neue&family=Roboto:wght@400;500;700&display=swap">
<style>
  :root {
    --navy: #1d4f8f;
    --navy-deep: #173f73;
    --ink: #1f1f1f;
    --muted: #555555;
    --paper: #ffffff;
    --frame: #3a3a3a;
    --photo-a: #8a7f74;
    --photo-b: #4d4a47;
    --portrait-a: #d9dde2;
    --portrait-b: #9aa3ad;
    --band: rgba(60, 60, 60, 0.55);
    --panel: rgba(25, 30, 40, 0.72);
  }
  * { margin: 0; padding: 0; box-sizing: border-box; }
  html, body { width: 797px; height: 1200px; overflow: hidden; background: #eeeeee; }
  .flyer {
    position: relative; width: 797px; height: 1200px;
    background: var(--paper); overflow: hidden;
    font-family: "Roboto", Arial, sans-serif; color: var(--ink);
  }
  .hero-photo {
    position: absolute; left: 0; top: 0; width: 797px; height: 620px;
    background: linear-gradient(160deg, var(--photo-a) 0%, #6e6258 45%, var(--photo-b) 100%);
    clip-path: polygon(0 0, 100% 0, 100% 80%, 0 100%);
  }
  .title-band {
    position: absolute; left: 0; top: 0; width: 797px; height: 200px;
    background: var(--band);
    clip-path: polygon(0 0, 100% 0, 100% 78%, 0 100%);
  }
  .title-rule {
    position: absolute; left: 0; top: 22px; width: 797px; height: 6px;
    background: repeating-linear-gradient(90deg, #fff 0 70px, transparent 70px 120px);
    opacity: 0.9;
  }
  .event-title {
    position: absolute; left: 70px; top: 62px;
    font-family: "Bebas Neue", Impact, sans-serif; font-size: 124px; line-height: 1;
    color: #fff; letter-spacing: 1px;
  }
  .event-info {
    position: absolute; left: 50px; top: 240px; width: 470px;
    padding: 20px 24px; background: var(--panel); color: #fff;
  }
  .event-tagline {
    font-family: "Bebas Neue", Impact, sans-serif; font-size: 40px; line-height: 1;
    letter-spacing: 1px;
  }
  .event-subject { font-size: 15px; font-weight: 500; margin: 6px 0 14px; }
  .event-details { display: grid; grid-template-columns: 92px 1fr; row-gap: 6px; font-size: 15px; }
  .event-details dt { font-weight: 700; color: #9fc1ee; text-transform: uppercase; font-size: 13px; padding-top: 2px; }
  .feature-photo {
    position: absolute; left: 545px; top: 410px; width: 190px; height: 190px;
    border-radius: 50%; border: 8px solid var(--frame);
    background: linear-gradient(150deg, #c9c4bc, #7b746d);
  }
  .speaker {
    position: absolute; left: 50px; width: 697px; height: 150px;
    display: flex; align-items: center; gap: 32px;
  }
  .speaker.reverse { flex-direction: row-reverse; }
  .speaker-photo {
    flex: 0 0 136px; height: 136px; border-radius: 50%;
    border: 5px solid var(--navy-deep);
    background: radial-gradient(circle at 50% 40%, var(--portrait-a), var(--portrait-b));
  }
  .speaker-text h2 { font-size: 24px; font-weight: 700; color: var(--navy); line-height: 1.15; }
  .speaker-meta { font-size: 14px; font-weight: 500; color: var(--muted); margin: 4px 0 6px; }
  .speaker-text p { font-size: 14.5px; line-height: 1.42; text-align: justify; }
  .sponsor {
    position: absolute; right: 40px; top: 1158px;
    display: flex; align-items: center; gap: 10px;
    font-size: 15px; font-weight: 700;
  }
  .sponsor-name { font-size: 26px; font-weight: 700; color: var(--ink); }
  .sponsor-mark { width: 14px; height: 14px; background: var(--navy); }
  .footer-band {
    position: absolute; left: 0; bottom: 0; width: 600px; height: 48px;
    background: var(--navy);
    clip-path: polygon(0 0, 100% 0, 92% 100%, 0 100%);
  }
</style>
</head>
<body>
<main class="flyer">
  <div class="hero-photo" role="img" aria-label="Photo of a seminar room with attendees seated at tables facing a presenter and screen"></div>
  <div class="title-band"></div>
  <div class="title-rule"></div>
  <h1 class="event-title">Training Event</h1>

  <section class="event-info">
    <p class="event-tagline">Commit To Be The Best!</p>
    <p class="event-subject">Marketing, Training &amp; Management for Multifamily Professionals</p>
    <dl class="event-details">
      <dt>Date</dt><dd>Thursday, October 16, 2025</dd>
      <dt>Time</dt><dd>9:00 AM – 1:00 PM</dd>
      <dt>Location</dt><dd>Lakeview Conference Center, Suite 200</dd>
      <dt>Cost</dt><dd>$79 per person · Lunch included</dd>
    </dl>
  </section>

  <div class="feature-photo" role="img" aria-label="Photo of a conference table session with microphones"></div>

  <section class="speaker" style="top:640px">
    <div class="speaker-photo" role="img" aria-label="Portrait of speaker Dana Mercer"></div>
    <div class="speaker-text">
      <h2>Marketing That Fills Units</h2>
      <p class="speaker-meta">Dana Mercer · 9:00 – 10:15 AM</p>
      <p>Learn proven digital and on-site strategies that drive qualified traffic, boost tours and turn leads into signed leases for your apartment community.</p>
    </div>
  </section>

  <section class="speaker reverse" style="top:805px">
    <div class="speaker-photo" role="img" aria-label="Portrait of speaker Marcus Hale"></div>
    <div class="speaker-text">
      <h2>Training Leasing Teams to Win</h2>
      <p class="speaker-meta">Marcus Hale · 10:30 – 11:45 AM</p>
      <p>Build a training program that sharpens sales skills, improves customer service and gives every leasing agent the confidence to close.</p>
    </div>
  </section>

  <section class="speaker" style="top:970px">
    <div class="speaker-photo" role="img" aria-label="Portrait of speaker Renee Castillo"></div>
    <div class="speaker-text">
      <h2>Management for Lasting Results</h2>
      <p class="speaker-meta">Renee Castillo · 12:00 – 1:00 PM</p>
      <p>Discover leadership habits that raise retention, control expenses and keep residents, owners and staff working toward the same goals.</p>
    </div>
  </section>

  <div class="sponsor">
    <span>Sponsored by</span>
    <span class="sponsor-name">VHP</span>
    <span class="sponsor-mark"></span>
  </div>
  <div class="footer-band"></div>
</main>
</body>
</html>
```